Flyer Fewo Borne
Trotz etlicher Änderungen immer Hilfsbereit und alle Wünsche wurden von Jonas 1A umgesetzt.
Zielgruppe
Sehr geehrte Damen und Herren, 01.12.25
wir werden jetzt gleich die Entscheidung treffen. Daher möchten wir uns bei Ihnen allen für die Entwürfe und gute Zusammenarbeit bedanken. Es war für uns recht schwierig den Gewinner festzulegen.
Mit freundlichen Grüßen
Familie Borne
Sehr geehrte Damen und Herren,
Nachtrag. Bitte weisen Sie auf das:
1. Hügelländer Kirschfest vom 21.02.26 - 06.04.26
2. Oldimerveranstaltungen
3. Ausschrank Federweiser / neuer Wein ab September 2026
4. viele regionale Weinfeste
hin.
zunächst möchten wir uns bei Ihnen für die bisherigen Entwürfe bedanken. Wir haben eben die Textdatei überarbeitet und neu abgespeichert. Bitte überarbeiten Sie Ihre Texte in den Entwürfen. Sie können auch gerne textliche Passagen kürzer fassen.
Wir bitten Sie, die Weinregion südliche Weinstrasse etwas mehr im Hintergrund hervorzuheben.
Wir melden uns wenn dann nach der Überarbeitung der Texte.
Mit freundlichem Gruß
Aufgabenstellung
Warmes Design, bezogen auf die Weinregion, hoher Freizeitwert, zentral gelegen. Bodenständig, da die Wohnung in einem Haus ausgebaut ist was keinerlei Grautöne hat. Das 2 Familienhaus ist im italienischen Stil gebaut

```html
<!DOCTYPE html>
<html lang="de">
<head>
<meta charset="utf-8">
<title>Flyer Fewo Borne</title>
<link href="https://fonts.googleapis.com/css2?family=Montserrat:wght@400;500;600;700&display=swap" rel="stylesheet">
<style>
:root{
  --plum:#743d60;
  --plum-dark:#5a2947;
  --plum-deep:#4e2240;
  --pink:#e2a3cd;
  --magenta:#b11d6b;
  --ink:#3a2a35;
  --grey:#6d6a6c;
  --paper:#ffffff;
  --stage:#ededed;
  --map:#6e5666;
}
*{margin:0;padding:0;box-sizing:border-box}
html,body{width:1000px;height:1200px;overflow:hidden;background:var(--stage);font-family:"Montserrat",Arial,sans-serif;color:var(--ink)}
.spread{position:absolute;left:100px;width:800px;height:564px;background:var(--paper);overflow:hidden;box-shadow:0 2px 10px rgba(0,0,0,.12)}
.spread--outer{top:24px}
.spread--inner{top:612px}
.shapes{position:absolute;inset:0}
.abs{position:absolute}
.photo{position:absolute;border-radius:12px;background:linear-gradient(160deg,#e9e3dc,#b9a896 70%,#8a6e58)}
.photo--bed{background:linear-gradient(160deg,#f1ece6,#d9cbbd 60%,#b58a5c)}
.photo--bath{background:linear-gradient(160deg,#e8eef2,#c4ccd3 60%,#8a9cab)}
.photo--living{background:linear-gradient(160deg,#f3efe9,#d6c6b3 60%,#9a7a5c)}
.panel-title{position:absolute;width:400px;text-align:center;font-weight:600;font-size:17px;color:#fff}
.panel-title--dark{color:var(--ink)}
.small{font-size:8px;line-height:1.3}
.white{color:#fff}
.price{position:absolute;font-size:17px;color:#fff;font-weight:400}
.price sup{font-size:7px}
.price .unit{font-size:7px;position:relative;top:3px}
.tag{position:absolute;font-size:7px;color:var(--plum-dark);text-align:center;width:74px}
.contact{position:absolute;font-size:8px;color:var(--ink);display:flex;align-items:center;gap:8px}
.contact svg{flex:none}
.sep{width:1px;height:10px;background:#bbb}
.cover-title{position:absolute;left:400px;width:400px;text-align:center;top:275px;font-size:30px;font-weight:700;color:var(--plum-deep)}
.cover-sub{position:absolute;left:400px;width:400px;text-align:center;top:317px;font-size:14px;font-weight:600;color:var(--magenta)}
.feature{position:absolute;top:370px;width:90px;text-align:center;font-size:9px;font-weight:600;line-height:1.2;color:var(--ink)}
.feature .icon{display:block;margin:0 auto 8px;width:36px;height:36px;border-radius:7px;background:var(--plum)}
.feature .icon svg{display:block;width:36px;height:36px}
.feature small{font-weight:400;font-size:9px}
.lead{position:absolute;left:400px;width:400px;text-align:center;top:478px;font-size:11.5px;line-height:1.2;color:var(--grey)}
.list-item{position:absolute;left:32px;display:flex;align-items:center;gap:12px;font-size:9.5px;line-height:1.25;color:#fff}
.list-item svg{flex:none}
.feat-list{position:absolute;left:440px;top:82px;width:340px;list-style:none}
.feat-list li{position:relative;padding-left:16px;font-size:9.5px;line-height:1.3;color:var(--ink);margin-bottom:12px}
.feat-list li::before{content:"";position:absolute;left:0;top:1px;width:10px;height:10px;border-radius:50%;background:var(--magenta)}
.feat-list li::after{content:"";position:absolute;left:3.3px;top:3px;width:2.5px;height:4.5px;border:solid #fff;border-width:0 1.4px 1.4px 0;transform:rotate(45deg)}
.feat-list .muted{color:#b58aa6}
.note{position:absolute;left:440px;width:340px;font-size:8px;line-height:1.3;color:var(--grey)}
</style>
</head>
<body>

<section class="spread spread--outer">
  <svg class="shapes" viewBox="0 0 800 564" aria-hidden="true">
    <defs>
      <linearGradient id="plumGrad" x1="0" y1="0" x2="1" y2="1">
        <stop offset="0" stop-color="#7b4466"/><stop offset="1" stop-color="#5a2947"/>
      </linearGradient>
    </defs>
    <path d="M352 0 H800 V262 C740 258 690 232 620 226 C540 220 470 240 410 222 Z" fill="url(#plumGrad)"/>
    <path d="M0 0 H352 C330 70 372 140 386 210 C400 280 418 318 398 333 C372 350 300 336 220 340 C150 344 60 344 0 344 Z" fill="url(#plumGrad)"/>
  </svg>
  <div class="abs" role="img" aria-label="Foto des Zweifamilienhauses im italienischen Stil mit Holztür und Rosen"
       style="left:352px;top:0;width:448px;height:212px;background:linear-gradient(180deg,#cfe3f2 0%,#f1e6cf 45%,#e3d4b4 75%,#6f7d4e 100%);clip-path:path('M8 0 H408 C392 40 440 80 440 130 C440 190 410 205 370 200 C290 190 210 190 118 205 C78 210 58 195 48 160 C33 110 14 60 8 0 Z')"></div>

  <h2 class="panel-title" style="top:20px;left:0">Preise &amp; Infos</h2>
  <p class="abs small white" style="left:28px;top:55px;width:275px">Im Mietpreis sind alle Nebenkosten, Endreinigung, Handtücher, Bettwäsche sowie der PKW-Stellplatz auf dem Grundstück enthalten. Ein E-Bike-Abstellplatz für max. 2 Räder ist in der Garage möglich.</p>
  <p class="abs small white" style="left:28px;top:116px;width:290px;font-weight:600">Die Preise gelten für 1-2 Personen und gelten für das Jahr 2026, ohne Verpflegung.</p>

  <div class="abs" style="left:133px;top:152px;width:74px;height:132px;border-radius:5px;background:var(--pink)"></div>
  <div class="abs" style="left:28px;top:196px;width:105px;height:1px;background:rgba(255,255,255,.25)"></div>
  <div class="abs" style="left:28px;top:240px;width:105px;height:1px;background:rgba(255,255,255,.25)"></div>
  <div class="price" style="left:49px;top:166px">110<sup>€</sup><span class="unit">/Nacht</span></div>
  <div class="price" style="left:52px;top:211px">85<sup>€</sup><span class="unit">/Nacht</span></div>
  <div class="price" style="left:50px;top:254px">80<sup>€</sup><span class="unit">/Nacht</span></div>
  <div class="tag" style="left:133px;top:174px">ab 2 Nächte</div>
  <div class="tag" style="left:133px;top:217px">ab 3-6 Nächte</div>
  <div class="tag" style="left:133px;top:259px">ab 7 Nächte</div>
  <div class="price" style="left:240px;top:211px">10<sup>€</sup><span class="unit">/Nacht</span></div>
  <div class="abs" style="left:293px;top:196px;width:82px;height:43px;border-radius:5px;background:var(--pink)"></div>
  <div class="tag" style="left:297px;top:217px">Ein Hund</div>
  <p class="abs white" style="left:224px;top:246px;font-size:7px">nach vorheriger Rücksprache</p>
  <p class="abs small white" style="left:28px;top:305px;font-weight:600">Jede weitere Person: 25 € pro Tag (Gültig für jede Aufenthaltsdauer.).</p>

  <div class="abs" role="img" aria-label="Kleine Deutschlandkarte mit Standortmarkierung in der Pfalz"
       style="left:357px;top:318px;width:30px;height:56px;background:var(--map);border-radius:45% 55% 40% 50%"></div>

  <div class="photo photo--living" role="img" aria-label="Foto Wohnbereich mit Schrankwand" style="left:28px;top:357px;width:98px;height:98px"></div>
  <div class="photo photo--bath" role="img" aria-label="Foto Abstellkammer mit Waschmaschine" style="left:141px;top:357px;width:98px;height:98px"></div>
  <div class="photo photo--living" role="img" aria-label="Foto Wohnzimmer mit Fenster" style="left:254px;top:357px;width:98px;height:98px"></div>

  <p class="abs small" style="left:28px;top:479px;color:var(--ink)">An um zu prüfen ob Sie an Ihrem Wunschdatum bei uns Urlaub machen können.</p>
  <div class="contact" style="left:28px;top:507px">
    <svg width="12" height="12" viewBox="0 0 12 12"><circle cx="6" cy="6" r="6" fill="#743d60"/><path d="M4 3.2l1 1.3-.6.8c.4.9 1 1.5 1.9 1.9l.8-.6 1.3 1-.6 1.1C5.6 8.5 3.5 6.4 3.3 4z" fill="#fff"/></svg>
    0170-5550142<span class="sep"></span>06341- 5550387</div>
  <div class="contact" style="left:232px;top:507px">
    <svg width="12" height="12" viewBox="0 0 12 12"><circle cx="6" cy="6" r="6" fill="#743d60"/><rect x="3" y="4" width="6" height="4.2" fill="none" stroke="#fff" stroke-width=".9"/><path d="M3 4l3 2.3L9 4" fill="none" stroke="#fff" stroke-width=".9"/></svg>
    stilmarkt@postfach.de</div>
  <div class="contact" style="left:28px;top:533px">
    <svg width="12" height="12" viewBox="0 0 12 12"><circle cx="6" cy="6" r="6" fill="#743d60"/><path d="M6 2.6a2 2 0 0 1 2 2c0 1.5-2 3.6-2 3.6S4 6.1 4 4.6a2 2 0 0 1 2-2z" fill="none" stroke="#fff" stroke-width=".9"/></svg>
    Rebenweg 6, 67480 Hügelbach, Deutschland</div>

  <h1 class="cover-title">Ferienwohnung Borne</h1>
  <p class="cover-sub">Ihre Auszeit in der „Toskana der Pfalz“</p>
  <div class="feature" style="left:427px"><span class="icon"><svg viewBox="0 0 36 36"><circle cx="18" cy="18" r="9" fill="none" stroke="#fff" stroke-width="1.4"/><path d="M14 18.2l3 3 5.5-6" fill="none" stroke="#fff" stroke-width="1.6"/></svg></span>nur für<br>Erwachsene</div>
  <div class="feature" style="left:526px"><span class="icon"><svg viewBox="0 0 36 36"><path d="M9 25V12M9 20h18v5M12 20v-4h6v4" fill="none" stroke="#fff" stroke-width="1.4"/></svg></span>bis zu<br>4 Personen</div>
  <div class="feature" style="left:626px"><span class="icon"><svg viewBox="0 0 36 36"><path d="M10 19h16a8 6 0 0 1-16 0z" fill="none" stroke="#fff" stroke-width="1.4"/><path d="M9 25h18" stroke="#fff" stroke-width="1.4"/></svg></span>Hund erlaubt<br><small>(gegen Aufpreis)</small></div>
  <div class="feature" style="left:718px"><span class="icon"><svg viewBox="0 0 36 36"><rect x="10" y="10" width="16" height="16" fill="none" stroke="#fff" stroke-width="1.4"/><path d="M14 22l8-8M18 14h4v4" fill="none" stroke="#fff" stroke-width="1.4"/></svg></span>ca. 76 m²</div>
  <p class="lead">Unsere lichtdurchflutete Ferienwohnung liegt im<br>Obergeschoss eines mediterranen Zweifamilienhauses<br>in Hügelbach – inmitten der Pfalz</p>
  <div class="contact" style="left:520px;top:532px">
    <svg width="12" height="12" viewBox="0 0 12 12"><circle cx="6" cy="6" r="6" fill="#743d60"/><path d="M4 3.2l1 1.3-.6.8c.4.9 1 1.5 1.9 1.9l.8-.6 1.3 1-.6 1.1C5.6 8.5 3.5 6.4 3.3 4z" fill="#fff"/></svg>
    0170-5550142<span class="sep"></span>06341- 5550387</div>
</section>

<section class="spread spread--inner">
  <svg class="shapes" viewBox="0 0 800 564" aria-hidden="true">
    <defs>
      <linearGradient id="plumGrad2" x1="0" y1="0" x2="1" y2="1">
        <stop offset="0" stop-color="#7b4466"/><stop offset="1" stop-color="#5a2947"/>
      </linearGradient>
    </defs>
    <rect x="0" y="0" width="400" height="564" fill="url(#plumGrad2)"/>
    <path d="M400 466 C470 450 520 470 600 462 C680 455 740 440 800 446 V564 H400 Z" fill="url(#plumGrad2)"/>
  </svg>
  <div class="abs" role="img" aria-label="Foto Wohnbereich mit Sofa, Fernseher und Esstisch"
       style="left:0;top:410px;width:400px;height:154px;background:linear-gradient(160deg,#f2eee9,#d8c8b6 55%,#8d6a4e);clip-path:path('M0 34 C60 10 110 48 170 34 C230 20 260 10 320 16 C360 20 385 14 400 8 V154 H0 Z')"></div>

  <h2 class="panel-title" style="top:30px;left:0">Lage &amp; Umgebung</h2>
  <div class="list-item" style="top:64px"><svg width="22" height="18" viewBox="0 0 22 18"><path d="M2 17V9l5-4 5 4v8M10 17V7l5-4 5 4v10M1 17h20" fill="none" stroke="#fff" stroke-width="1.2"/></svg>Ruhige Lage in einem kleinen Wohngebiet</div>
  <div class="list-item" style="top:103px"><svg width="22" height="18" viewBox="0 0 22 18"><path d="M3 3v14M8 3v14M14 3v14M19 3v14M1 6h20M1 17h20" fill="none" stroke="#fff" stroke-width="1.2"/></svg>Weingüter, Weinstuben und Restaurants in kurzer Entfernung</div>
  <div class="list-item" style="top:136px"><svg width="22" height="20" viewBox="0 0 22 20"><path d="M6 1a4 4 0 0 1 4 4c0 3-4 7-4 7S2 8 2 5a4 4 0 0 1 4-4zM14 14a3 3 0 1 0 6 0a3 3 0 1 0-6 0M6 14h8" fill="none" stroke="#fff" stroke-width="1.2"/></svg>Pfälzerwald ca. 10 km, Elsass/Frankreich ca. 38 km,<br>Speyer ca. 23 km</div>
  <div class="list-item" style="top:176px"><svg width="22" height="20" viewBox="0 0 22 20"><path d="M2 19V9h8v10M6 9V4M12 19V11h8v8M16 11V6M1 19h20" fill="none" stroke="#fff" stroke-width="1.2"/></svg>Ideal für Spaziergänge, Radtouren, Weinproben<br>und Ausflüge an den Rhein</div>

  <h2 class="panel-title" style="top:230px;left:0">Veranstaltungen &amp; Highlights 2026</h2>
  <div class="list-item" style="top:274px"><svg width="22" height="20" viewBox="0 0 22 20"><circle cx="11" cy="10" r="3" fill="none" stroke="#fff" stroke-width="1.2"/><circle cx="11" cy="10" r="8" fill="none" stroke="#fff" stroke-width="1.2"/></svg>Hügelländer Kirschfest vom 21. Februar 2026 bis zum<br>6. April 2026</div>
  <div class="list-item" style="top:314px"><svg width="22" height="18" viewBox="0 0 22 18"><path d="M2 12h18v-3l-3-4H7L4 9H2zM6 15a2 2 0 1 0 0-.1M16 15a2 2 0 1 0 0-.1" fill="none" stroke="#fff" stroke-width="1.2"/></svg>Oldtimer-Events in der Region</div>
  <div class="list-item" style="top:346px"><svg width="22" height="20" viewBox="0 0 22 20"><path d="M6 1v5l-2 3v10h5V9L7 6M14 6h6l-1 5a2 2 0 0 1-4 0zM17 13v6M14 19h6" fill="none" stroke="#fff" stroke-width="1.2"/></svg>Neuer Wein (Federweiser) / New Wine verfügbar<br>ab September 2026</div>
  <div class="list-item" style="top:390px"><svg width="22" height="18" viewBox="0 0 22 18"><path d="M2 17V6h18v11zM2 6l3-4M20 6l-3-4M6 10h10" fill="none" stroke="#fff" stroke-width="1.2"/></svg>Viele regionale Weinfeste</div>

  <h2 class="panel-title panel-title--dark" style="top:30px;left:400px">Ihre Ferienwohnung auf einen Blick</h2>
  <ul class="feat-list">
    <li>Wohn-Essbereich mit Sofa, Esstisch und TV</li>
    <li>Schlafzimmer mit Boxspringbett und großem Kleiderschrank</li>
    <li>Einbauküche mit Kochinsel, Herd, Backofen, Kühlschrank mit Gefrierfach, Geschirrspüler und Kaffeevollautomat</li>
    <li>Bad mit Badewanne und Dusche mit Sitzbank;<br>separates Gäste-WC im Erdgeschoss</li>
    <li>Zwei überdachte Balkone, einer davon als Sonnenbalkon</li>
    <li>Waschmaschine und Wäscheständer</li>
    <li>Kostenloses WLAN <span class="muted">(Nutzung auf eigene Gefahr)</span>, Pkw-Stellplatz auf dem Grundstück, Abstellmöglichkeit für E-Bikes/Fahrräder in der Garage</li>
  </ul>
  <div class="abs" style="left:468px;top:324px;display:flex;align-items:center;gap:6px;font-size:8px;color:var(--ink)">
    <svg width="24" height="24" viewBox="0 0 24 24"><circle cx="12" cy="12" r="11" fill="#743d60"/><circle cx="12" cy="12" r="7" fill="none" stroke="#fff" stroke-width="1.2"/><path d="M12 8v5M12 15v1" stroke="#fff" stroke-width="1.5"/></svg>
    Nichtraucherwohnung – Rauchen nur auf den Balkonen
  </div>
  <p class="note" style="top:369px">Eine kleine Abstellkammer mit Bügelbrett, Bügeleisen sowie mobilem Wäscheständer ist vorhanden.</p>
  <p class="note" style="top:407px">Alles im Jahr 2024 /25 fertig gestellt in einem kleinen Wohngebiet<br>aus dem Jahr 2016 ganz nah an den Weinreben.</p>

  <div class="photo photo--bed" role="img" aria-label="Foto Schlafzimmer mit Boxspringbett" style="left:440px;top:440px;width:98px;height:96px"></div>
  <div class="photo photo--bath" role="img" aria-label="Foto Badezimmer mit Badewanne" style="left:559px;top:440px;width:98px;height:96px"></div>
  <div class="photo photo--living" role="img" aria-label="Foto Küche mit Kochinsel" style="left:678px;top:440px;width:98px;height:96px"></div>
</section>

</body>
</html>
```